Modern looking signage for dental office.

Exterior signage for passing cars
Target Market(s)
Cars passing by
Font styles to use
Sans Serif
Colors
3276b5
Requirements
Must have
- Logo
- OPEN ON SUTURDAY AND SUNDAY
- NIGHT CLINIC AVAILABLE
- PLEASE USE THE FONT TYPE IN FILE 4 UPLOADED BELOW.
- (482) 730-2964
- Modern looking

```html
<!DOCTYPE html>
<html lang="en">
<head>
<meta charset="utf-8">
<title>Arbor Dental – Exterior Sign</title>
<link href="https://fonts.googleapis.com/css2?family=Anton&family=Montserrat:wght@400&display=swap" rel="stylesheet">
<style>
  :root {
    --brand-blue: #0c5598;
    --panel-white: #ffffff;
    --ink-dark: #3b3634;
    --ink-black: #141414;
    --backdrop: #e6e7e8;
  }
  * { margin: 0; padding: 0; box-sizing: border-box; }
  html, body { width: 1200px; height: 1200px; overflow: hidden; }
  body { background: var(--backdrop); position: relative; font-family: "Montserrat", sans-serif; }

  .sign-panel {
    position: absolute;
    left: 110px;
    width: 980px;
    background: var(--panel-white);
    overflow: hidden;
    box-shadow: 0 6px 18px rgba(0,0,0,0.12);
  }
  .sign-main { top: 170px; height: 620px; }
  .sign-strip { top: 830px; height: 170px; }

  .accent-shape { position: absolute; inset: 0; width: 100%; height: 100%; }

  .brand-lockup {
    position: absolute;
    left: 70px;
    top: 100px;
    display: flex;
    align-items: center;
    gap: 34px;
  }
  .brand-mark {
    width: 170px; height: 170px;
    border: 3px solid var(--ink-dark);
    border-radius: 50%;
    flex: none;
  }
  .brand-name {
    font-family: "Montserrat", sans-serif;
    font-weight: 400;
    font-size: 78px;
    letter-spacing: 2px;
    color: var(--ink-dark);
    line-height: 1;
    white-space: nowrap;
  }
  .brand-tagline {
    font-family: "Montserrat", sans-serif;
    font-weight: 400;
    font-size: 31px;
    color: var(--ink-dark);
    letter-spacing: 0.5px;
    margin-top: 18px;
    white-space: nowrap;
  }

  .headline {
    position: absolute;
    right: 40px;
    bottom: 50px;
    font-family: "Anton", sans-serif;
    font-weight: 400;
    font-size: 94px;
    line-height: 1.15;
    color: var(--panel-white);
    text-align: right;
    letter-spacing: 1.5px;
  }

  .phone {
    position: absolute;
    left: 30px;
    top: 50%;
    transform: translateY(-50%);
    font-family: "Anton", sans-serif;
    font-size: 58px;
    color: var(--ink-black);
    letter-spacing: 1px;
    white-space: nowrap;
  }
  .weekend-hours {
    position: absolute;
    right: 30px;
    top: 50%;
    transform: translateY(-50%);
    font-family: "Anton", sans-serif;
    font-size: 46px;
    line-height: 1.2;
    color: var(--panel-white);
    text-align: right;
    letter-spacing: 1px;
    white-space: nowrap;
  }
</style>
</head>
<body>
  <section class="sign-panel sign-main">
    <svg class="accent-shape" viewBox="0 0 980 620" preserveAspectRatio="none" aria-hidden="true">
      <polygon points="300,330 980,330 980,620 420,620" fill="var(--brand-blue)"/>
    </svg>
    <div class="brand-lockup">
      <div class="brand-mark"></div>
      <div class="brand-text">
        <div class="brand-name">ARBOR DENTAL</div>
        <div class="brand-tagline">MODERN GENERAL DENTISTRY</div>
      </div>
    </div>
    <h1 class="headline">Night Clinic<br>Available</h1>
  </section>

  <section class="sign-panel sign-strip">
    <svg class="accent-shape" viewBox="0 0 980 170" preserveAspectRatio="none" aria-hidden="true">
      <polygon points="430,0 980,0 980,170 490,170" fill="var(--brand-blue)"/>
    </svg>
    <p class="phone">(482) 730-2964</p>
    <p class="weekend-hours">Open on<br>Saturday and Sunday</p>
  </section>
</body>
</html>
```